Quiet-Harbor charity auctions

We need a three part design for a nonprofit charity auction platform. This platform will eventually interface with a cell phone app, therefore the initial design needs to be responsive. Each phase should produce a working web page that builds upon the previous phase. The first phase is strictly to be a content page which can present our Clavenro channel. It should also be a direct link between our alternate social media resources, e.g. KL, Quillo, Vellomar etc. We can afford $500 for each phase (total $1500). Only serious long-term designers need respond.

Target Market(s)

High profile celebrities
International Bidders
Social Media

Industry/Entity Type

Cell Phone

Number of Pages Required

5+ page

Requirements
Must have
• Logos
• Responsive between desktop and cell phone website
• Upgradeable
• Hyper text
• Blog
• Flash (with video and image storage) i.e. Clavenro, Vellomar, Tandrelo etc.
• Background music
Nice to have
• Intuitive with action buttons e.g. automatic post buttons, play buttons, stop buttons etc

```html
<!DOCTYPE html>
<html lang="en">
<head>
<meta charset="utf-8">
<title>Quiet-Harbor Charity Auctions</title>
<link rel="stylesheet" href="https://fonts.googleapis.com/css2?family=Open+Sans:ital,wght@0,400;0,600;1,400&display=swap">
<style>
:root{
  --brand-red:#c0001b;
  --ink:#111;
  --muted:#8a8a8a;
  --panel:#efefef;
  --white:#fff;
  --black:#000;
}
*{box-sizing:border-box;margin:0;padding:0}
html,body{width:1200px;height:2426px;overflow:hidden;background:var(--white)}
body{font-family:"Open Sans",Arial,sans-serif;color:var(--ink);position:relative}
.site-header{position:absolute;left:0;top:0;width:1200px;height:141px}
.brand{position:absolute;left:60px;top:40px;display:flex;align-items:center;gap:14px}
.brand-mark{width:52px;height:52px;border-radius:50%;background:var(--ink)}
.brand-name{font-size:24px;font-weight:600;letter-spacing:3px;color:var(--ink)}
.search{position:absolute;left:909px;top:79px;width:229px;height:50px;border:1px solid #9a9a9a;display:flex;align-items:center;padding:0 10px;font-size:13px;color:#777;justify-content:space-between}
.main-nav{position:absolute;left:0;top:141px;width:1200px;height:64px;background:var(--brand-red)}
.main-nav a{position:absolute;top:0;height:64px;line-height:64px;color:var(--white);text-decoration:none;font-size:17px;transform:translateX(-50%)}
.main-nav .active{left:60px;width:116px;background:var(--black);text-align:center;transform:none}
.main-nav .account{left:auto;right:62px;transform:none;text-decoration:underline}
.hero{position:absolute;left:0;top:205px;width:1200px;height:539px;background:radial-gradient(circle at 50% 45%,#a8e060 0%,#5cb82a 40%,#2f8a16 75%,#e8f3dc 100%)}
.hero-arrow{position:absolute;top:262px;width:48px;height:48px}
.hero-arrow.prev{left:36px}.hero-arrow.next{left:1114px}
.section-title{font-size:27px;font-weight:400;text-align:center;position:absolute;left:0;width:1200px}
.welcome-text{position:absolute;left:220px;width:760px;top:820px;text-align:center;font-size:17px;line-height:22px;color:var(--muted)}
.btn{position:absolute;color:var(--white);font-size:16px;text-align:center;text-decoration:none}
.btn-more{left:543px;top:893px;width:113px;height:40px;line-height:40px;background:var(--brand-red)}
.products{position:absolute;left:0;top:970px;width:1200px;height:486px;background:var(--panel)}
.product{position:absolute;top:78px;width:344px;text-align:center}
.product-image{width:344px;height:235px}
.product h3{font-weight:400;font-size:18px;color:var(--brand-red);margin-top:20px}
.product p{font-size:13.5px;line-height:22px;color:var(--muted);margin-top:8px;padding:0 30px}
.video{position:absolute;left:239px;top:1546px;width:720px;height:359px}
.video-frame{width:720px;height:319px;background:radial-gradient(circle at 45% 45%,#7a5a48 0%,#3a2a24 55%,#1e1614 100%)}
.btn-watch{left:537px;top:1952px;width:126px;height:44px;line-height:44px;background:var(--black)}
.blog{position:absolute;left:0;top:2050px;width:1200px;height:292px;background:var(--panel)}
.post{position:absolute;top:97px;display:flex;gap:22px}
.post-image{width:204px;height:154px;flex:none}
.post h4{font-size:13.5px;font-weight:600;margin-top:10px}
.post p{font-size:13.5px;line-height:22px;color:#666;margin-top:4px;width:280px}
.post time{display:block;font-size:13.5px;font-style:italic;color:var(--brand-red);margin-top:6px}
.post a{font-size:17px;color:#1e4e1e;text-decoration:underline}
.site-footer{position:absolute;left:0;top:2342px;width:1200px;height:84px;background:var(--brand-red);color:var(--white)}
.copyright{position:absolute;left:60px;top:30px;font-size:15px;font-weight:600}
.social{position:absolute;right:60px;top:27px;display:flex;gap:20px}
.social a{color:var(--white);text-decoration:none;font-size:16px;font-weight:600;display:flex;align-items:center;gap:6px}
.social a::before{content:"";width:12px;height:12px;background:var(--white)}
</style>
</head>
<body>
<header class="site-header">
  <div class="brand"><span class="brand-mark"></span><span class="brand-name">QUIET-HARBOR</span></div>
  <div class="search"><span>SEARCH</span>
    <svg width="22" height="22" viewBox="0 0 22 22"><circle cx="9" cy="9" r="6.5" fill="none" stroke="#777" stroke-width="2.5"/><line x1="14" y1="14" x2="20" y2="20" stroke="#777" stroke-width="3"/></svg>
  </div>
</header>
<nav class="main-nav">
  <a class="active" href="#">HOME</a>
  <a href="#" style="left:278px">ABOUT US</a>
  <a href="#" style="left:430px">BLOG</a>
  <a href="#" style="left:600px">OUR SERVICES</a>
  <a href="#" style="left:796px">CONTACT US</a>
  <a class="account" href="#">SIGN IN/ REGISTER</a>
</nav>
<section class="hero" role="img" aria-label="Pile of faceted green gemstones with one red oval gem at the centre">
  <svg class="hero-arrow prev" viewBox="0 0 48 48"><circle cx="24" cy="24" r="24" fill="#111"/><polyline points="28,13 17,24 28,35" fill="none" stroke="#fff" stroke-width="5"/></svg>
  <svg class="hero-arrow next" viewBox="0 0 48 48"><circle cx="24" cy="24" r="24" fill="#111"/><polyline points="20,13 31,24 20,35" fill="none" stroke="#fff" stroke-width="5"/></svg>
</section>
<h1 class="section-title" style="top:772px">WELCOME TO OUR SITE !!!</h1>
<p class="welcome-text">Dipisicing elit sed do eiusmodporincididunt ut labore et dolore magna aliqua. Ut enim ad minim veniam quis. nostrud exercitation des ullamco laboris massanisi ut aliquip.”</p>
<a class="btn btn-more" href="#">MORE</a>
<section class="products">
  <h2 class="section-title" style="top:26px">OUR PRODUCTS</h2>
  <div class="product" style="left:60px">
    <div class="product-image" role="img" aria-label="Antique chaise longue in a dim grey room" style="background:linear-gradient(#5a5652,#2e2b29)"></div>
    <h3>EPSUM FACTORIAL</h3>
    <p>Aenean nonummy hendrerit mauris. Phasellus porta. Fusce suscipit varius mum sociis natoque penatibus et magnis dis parturient...</p>
  </div>
  <div class="product" style="left:427px">
    <div class="product-image" role="img" aria-label="Gilded armchair with golden upholstery beside a small table" style="background:radial-gradient(circle at 55% 55%,#e0a82a,#8a4e14 70%,#3a1e0a)"></div>
    <h3>QUID PRO QUO</h3>
    <p>Aenean nonummy hendrerit mauris. Phasellus porta. Fusce suscipit varius mum sociis natoque penatibus et magnis dis parturient...</p>
  </div>
  <div class="product" style="left:794px">
    <div class="product-image" role="img" aria-label="Strands of green beads and silver jewellery pieces" style="background:radial-gradient(circle at 50% 50%,#3a9a78,#1a4a3e 65%,#0e2620)"></div>
    <h3>EPSUM FACTORIAL</h3>
    <p>Aenean nonummy hendrerit mauris. Phasellus porta. Fusce suscipit varius mum sociis natoque penatibus et magnis dis parturient...</p>
  </div>
</section>
<h2 class="section-title" style="top:1482px">FEATURED PROJECTS</h2>
<div class="video">
  <div class="video-frame" role="img" aria-label="Clavenro video still of a jeweller polishing a ring set with a purple stone"></div>
  <svg width="720" height="40" viewBox="0 0 720 40">
    <rect width="720" height="40" fill="#2a2a2a"/>
    <polygon points="20,14 20,26 30,20" fill="#fff"/>
    <rect x="70" y="17" width="500" height="6" fill="#555"/>
    <rect x="70" y="17" width="272" height="6" fill="#5a9ad8"/>
    <polygon points="593,17 597,17 602,12 602,28 597,23 593,23" fill="#ddd"/>
    <rect x="616" y="17" width="80" height="6" fill="#555"/>
    <rect x="616" y="17" width="60" height="6" fill="#5a9ad8"/>
  </svg>
</div>
<a class="btn btn-watch" href="#">WATCH IT</a>
<section class="blog">
  <h2 class="section-title" style="top:30px">OUR BLOG</h2>
  <article class="post" style="left:60px">
    <div class="post-image" role="img" aria-label="Hanging strands of colourful beads" style="background:linear-gradient(90deg,#6a4a2a,#b08a4a,#3a5a8a,#7a3a3a)"></div>
    <div>
      <h4>LOREM IPSUM DOLOR SIT AMET, COSECTETU.</h4>
      <p>Lorem ipsum dolor sit amet, consectetuer adi piscing elit, sed diam nonummy nibh euismod tincidunt ut laoree.</p>
      <time>MONDAY, 12 JANUARY 2015</time>
      <a href="#">Read More</a>
    </div>
  </article>
  <article class="post" style="left:632px">
    <div class="post-image" role="img" aria-label="Row of carved wooden chairs with colourful seats" style="background:linear-gradient(#f4ece4,#c0502a 60%,#6a8aa0)"></div>
    <div>
      <h4>LOREM IPSUM DOLOR SIT AMET, COSECTETU.</h4>
      <p>Lorem ipsum dolor sit amet, consectetuer adi piscing elit, sed diam nonummy nibh euismod tincidunt ut laoree.</p>
      <time>MONDAY, 12 JANUARY 2015</time>
      <a href="#">Read More</a>
    </div>
  </article>
</section>
<footer class="site-footer">
  <p class="copyright">quiet harbor charity auction @ 2015 All copyrights reserved.</p>
  <nav class="social">
    <a href="#">KL</a><a href="#">Tandrelo</a><a href="#">Quillo</a><a href="#">Plusora</a>
  </nav>
</footer>
</body>
</html>
```